Interior Design & Furniture E commerce Website Design

I need a cutting edge website design, this is for Interior Design Services as well as eCommerce for furniture and home decor www.lorivelhomestudio.com
Here is a sample of the concept behind the site.
I am a furniture & Interior Designer, want to create a life style brand.
Will offer Interior Design Services : Commercial & Residential (this portion will be a catalog or portfolio type)
The eCommerce side will sell, Furniture, Lighting, Decor, Gifts, Textiles, will also be offering trade so that could be at bottom of site. I also like the concept of concierge as where all the info falls under: shipping, etc..

*Please make sure to make the eCommerce prominent.

Hello Designers, I also would like to possibly update my logo, the current one I like but don't Love.

Target Market(s)

High end customers with disposable income, who also appreciate quality and unique furniture & design

Number of Pages Required

5+ page

Colors
0255a3
f37122

Requirements
Must have
• Room Planer: I will be using this tool http://qtstudio.varnelbex.com/room-planner.inc
• Live Chat
• Will be offering 3d renderings for spaces as well as Virtual Reality
• The image I loaded that looks like copper, I would like to have that as a color on the site with the texture: so the colors are Blue and copper. Would like the site to be user friendly and interactive
• http://qtstudio.varnelbex.com/ (this is the current site in development, so we will be offering Design your own, Trends, inspiration, etc...
• I have included a headshot to use for now about me. or about us.
• I also included several actual project installation (residential and commercial) as well as a variety of my furniture items
• I have Included an old Bio and some articles I would like to show case in a Press Area
• I would also like to include a section for Events (Giving back )I do a lot of charity events 1-2 a year and would like to showcase that as well
• *Please make the store (ecommerce prominent )

```html
<!DOCTYPE html>
<html lang="en">
<head>
<meta charset="utf-8">
<title>Lorivel Home Studio — Interior Design &amp; Furniture</title>
<link rel="stylesheet" href="https://fonts.googleapis.com/css2?family=Jost:wght@400;500;600;700&family=Open+Sans:wght@400;600&display=swap">
<style>
:root{
  --blue:#0255a3;
  --blue-deep:#0a4c96;
  --orange:#f37122;
  --navy:#0f1f3a;
  --slate:#3c4668;
  --slate-light:#4a5478;
  --ink:#2b2f38;
  --muted:#6a6f78;
  --paper:#ffffff;
  --mist:#f4f4f5;
  --line:#d9dadd;
  --head:"Jost",sans-serif;
  --body:"Open Sans",sans-serif;
}
*{margin:0;padding:0;box-sizing:border-box}
html,body{width:1200px;height:3550px;overflow:hidden}
body{position:relative;background:var(--paper);font-family:var(--body);color:var(--ink)}
.abs{position:absolute}
.img{position:absolute;display:block}

/* buttons */
.btn{position:absolute;display:flex;align-items:center;justify-content:center;gap:8px;
  font-family:var(--head);font-weight:700;font-size:14px;letter-spacing:.5px;color:#fff;text-transform:uppercase;
  clip-path:polygon(0 0,88% 0,100% 50%,88% 100%,0 100%)}
.btn--orange{background:var(--orange)}
.btn--blue{background:var(--blue)}
.btn--pill{clip-path:polygon(8% 0,88% 0,100% 50%,88% 100%,8% 100%,0 50%)}

/* hero */
.hero{position:absolute;left:0;top:0;width:1200px;height:682px;
  background:linear-gradient(180deg,#2a211b 0%,#4a3628 40%,#5b3b2c 75%,#3b2820 100%)}
.hero__shade{position:absolute;inset:0;background:linear-gradient(90deg,rgba(20,14,10,.55),rgba(20,14,10,.15) 60%,rgba(20,14,10,.35))}
.brand{position:absolute;left:24px;top:20px;display:flex;align-items:center;gap:10px;
  font-family:var(--head);font-weight:600;font-size:15px;line-height:1.1;color:#fff;letter-spacing:1px;text-transform:uppercase}
.brand__mark{width:14px;height:14px;border:2px solid #fff}
.nav{position:absolute;left:405px;top:36px;display:flex;gap:34px;font-family:var(--head);font-size:13px;font-weight:500;color:#fff;text-transform:uppercase}
.nav a{color:#fff;text-decoration:none}
.nav .is-active{color:var(--orange)}
.hero__title{position:absolute;left:230px;top:252px;width:440px;font-family:var(--head);font-weight:600;font-size:36px;line-height:1.15;color:#fff}
.hero__text{position:absolute;left:230px;top:350px;width:400px;font-size:12px;line-height:1.45;color:#eee}
.thumbs{position:absolute;left:748px;top:640px;display:flex;gap:8px}
.thumb{width:70px;height:70px;border-radius:50%;border:4px solid #fff;box-shadow:0 2px 6px rgba(0,0,0,.3)}

/* section headings */
.sec-title{position:absolute;left:0;width:1200px;text-align:center;font-family:var(--head);font-weight:700;font-size:26px;letter-spacing:.5px;color:var(--navy);text-transform:uppercase}
.sec-lede{position:absolute;left:300px;width:600px;text-align:center;font-size:11px;line-height:1.5;color:var(--muted)}

/* about */
.about__title{left:237px;width:407px;top:758px}
.about__text{position:absolute;left:237px;top:805px;width:407px;text-align:center;font-size:11px;line-height:1.55;color:var(--muted)}
.hex{clip-path:polygon(25% 0,75% 0,100% 50%,75% 100%,25% 100%,0 50%)}
.about__frame{position:absolute;left:648px;top:757px;width:318px;height:286px;background:var(--line)}
.about__photo{left:6px;top:6px;width:306px;height:274px;background:linear-gradient(160deg,#7a5a3e,#b9825a 45%,#8c3a2b 75%,#5a4030)}

/* services */
.services{position:absolute;left:0;top:1089px;width:1200px;height:315px;background:linear-gradient(120deg,#4a4848,#6b6764 50%,#4d4a47)}
.services__shade{position:absolute;inset:0;background:rgba(30,30,32,.45)}
.service{position:absolute;top:38px;width:360px;height:200px;border:4px solid #fff}
.service__photo{inset:0;width:100%;height:100%}
.service__badge{position:absolute;top:192px;width:238px;height:86px;display:flex;align-items:center;justify-content:center;text-align:center;
  font-family:var(--head);font-weight:700;font-size:24px;line-height:1.05;color:#fff;text-transform:uppercase;border:3px solid #fff}

/* products */
.products{position:absolute;left:0;top:1404px;width:1200px;height:483px;background:linear-gradient(180deg,#fafafa,#f1f1f2)}
.showcase{position:absolute;left:346px;top:163px;width:556px;height:243px;background:var(--line)}
.showcase__inner{left:3px;top:3px;width:550px;height:237px;background:#fff}
.sofa{left:85px;top:40px;width:380px;height:160px;background:linear-gradient(180deg,#3c52a0,#28397a);border-radius:6px}
.arrow-btn{position:absolute;top:266px;width:38px;height:38px}

/* grid */
.tile{position:absolute;overflow:hidden}
.tile__title{font-family:var(--head);font-weight:700;font-size:22px;line-height:1.05;text-transform:uppercase}
.tile__text{font-size:10.5px;line-height:1.45;margin-top:8px}
.tile__more{display:inline-flex;align-items:center;gap:6px;font-family:var(--head);font-weight:700;font-size:12px;margin-top:12px;text-transform:uppercase}
.tile--light{background:var(--mist);color:var(--navy)}
.tile--light .tile__text{color:var(--muted)}
.tile--slate{background:var(--slate);color:#fff}
.tile--blue{background:var(--blue);color:#fff}
.tile--orange{background:var(--orange);color:#fff}
.tile--white{background:#fff;color:var(--navy)}
.tile--white .tile__text{color:var(--muted)}

/* news */
.news-card{position:absolute;top:2639px;width:237px}
.news-card__photo{position:relative;width:237px;height:270px}
.news-card__meta{position:absolute;left:0;bottom:0;width:237px;height:32px;background:var(--orange);color:#fff;
  display:flex;align-items:center;gap:14px;padding-left:58px;font-size:9.5px;font-weight:600;text-transform:uppercase}
.news-card__avatar{position:absolute;left:10px;bottom:4px;width:38px;height:38px;border-radius:50%;border:3px solid #fff;background:#c7b9a8}
.news-card__title{margin-top:20px;font-family:var(--head);font-weight:700;font-size:19px;line-height:1.1;color:var(--navy);text-transform:uppercase}

/* contact */
.contact{position:absolute;left:0;top:3030px;width:1200px;height:390px;background:linear-gradient(120deg,#3a2a22,#5a4234 50%,#3e2c24)}
.contact__shade{position:absolute;inset:0;background:rgba(18,14,12,.62)}
.contact .sec-title{color:#fff}
.contact .sec-lede{color:#ddd}
.field{position:absolute;width:359px;height:32px;border:1px solid rgba(255,255,255,.45);background:rgba(0,0,0,.15);
  padding:9px 10px;font-size:9.5px;color:#ddd;text-transform:uppercase}
.field--message{left:611px;top:151px;width:357px;height:117px}

/* footer */
.footer{position:absolute;left:0;top:3420px;width:1200px;height:130px;background:#fff}
.footer__links{position:absolute;top:32px;width:1200px;display:flex;justify-content:center;gap:14px;font-size:11px;color:var(--ink)}
.footer__links span.sep{color:#aaa}
.footer__copy{position:absolute;top:57px;width:1200px;text-align:center;font-size:10.5px;color:var(--muted)}
.footer__social{position:absolute;top:82px;width:1200px;display:flex;justify-content:center;gap:6px}
.footer__social span{width:18px;height:18px;border-radius:50%;background:var(--slate)}
</style>
</head>
<body>

<!-- HERO -->
<header class="hero">
  <div class="img hero__shade" role="img" aria-label="Photograph of a warm furnished patio lounge with fireplace, armchairs and patterned rugs"></div>
  <div class="brand"><span class="brand__mark"></span>Lorivel Home Studio</div>
  <nav class="nav">
    <a class="is-active">Home</a><a>About Us</a><a>Our Services</a><a>Shop</a><a>Blog</a><a>Contact Us</a>
  </nav>
  <a class="btn btn--blue btn--pill" style="left:913px;top:28px;width:110px;height:34px;font-size:12px">
    <svg width="12" height="11" viewBox="0 0 12 11"><path d="M0 1h2l1.6 6h6.4L11.5 2.5H3" fill="none" stroke="#fff" stroke-width="1.3"/><circle cx="4.5" cy="9.5" r="1" fill="#fff"/><circle cx="9" cy="9.5" r="1" fill="#fff"/></svg>Cart</a>
  <a class="btn btn--orange btn--pill" style="left:1041px;top:28px;width:126px;height:34px;font-size:12px">
    <svg width="12" height="11" viewBox="0 0 12 11"><path d="M1 1h10v6H5l-3 3V7H1z" fill="none" stroke="#fff" stroke-width="1.3"/></svg>Live Chat</a>

  <h1 class="hero__title">Lorem Ipsum Dolor Consectetur Adipiscing</h1>
  <p class="hero__text">Lorem ipsum dolor sit amet, consectetur adipiscing elit. Vestibulum vestibulum risus in enim accumsan porttitor sed eu orci. Curabitur in turpis eleifend, consectetur quam in, convallis urna.</p>
  <a class="btn btn--orange" style="left:230px;top:428px;width:162px;height:38px">Read More</a>

  <div class="thumbs">
    <div class="thumb" style="background:linear-gradient(135deg,#c9b08a,#7e6a4f)" role="img" aria-label="Thumbnail of a terrace lounge"></div>
    <div class="thumb" style="background:linear-gradient(135deg,#d08a4c,#8a4424)" role="img" aria-label="Thumbnail of a warm-toned dining room"></div>
    <div class="thumb" style="background:linear-gradient(135deg,#e4dccf,#a49a88)" role="img" aria-label="Thumbnail of a bright living room"></div>
  </div>
</header>

<!-- ABOUT -->
<section>
  <h2 class="sec-title about__title">About Us</h2>
  <p class="about__text">As a child, Lori Velhaven would spend quality time with her father by helping out in his furniture manufacturing company. She was delighted to be taken along on project installations to exciting places like hotels in Las Vegas. What began as a fun after school activity evolved into a passion for quality craftsmanship and unique furniture. Today her company, Harborline Hospitality Design, is thriving in the hospitality and residential trade industries.</p>
  <a class="btn btn--blue" style="left:331px;top:973px;width:160px;height:40px">Learn More</a>
  <div class="about__frame hex">
    <div class="img about__photo hex" role="img" aria-label="Photograph of a richly decorated living room with stone fireplace and patterned armchairs"></div>
  </div>
</section>

<!-- SERVICES -->
<section class="services">
  <div class="img services__shade" role="img" aria-label="Blurred photograph of a design studio workspace"></div>
  <div class="service" style="left:234px">
    <div class="img service__photo" style="background:linear-gradient(135deg,#3a2a1e,#7a5a3a 50%,#2e2620)" role="img" aria-label="Photograph of a commercial restaurant interior with chandelier"></div>
  </div>
  <div class="service__badge btn--blue hex" style="left:293px;top:1281px;position:absolute;top:192px;background:var(--blue)">Commercial<br>Design</div>
  <div class="service" style="left:613px">
    <div class="img service__photo" style="background:linear-gradient(135deg,#8c7a68,#5aa0a0 45%,#b88a60 75%,#6a5a50)" role="img" aria-label="Mood board of fabric swatches and material samples for a residential project"></div>
  </div>
  <div class="service__badge hex" style="left:675px;background:var(--orange)">Residential<br>Design</div>
</section>

<!-- PRODUCTS -->
<section class="products">
  <h2 class="sec-title" style="top:58px">Our Products</h2>
  <p class="sec-lede" style="top:93px">Lorem ipsum dolor sit amet, consectetur adipiscing elit. Vestibulum vestibulum risus in enim accumsan porttitor sed eu orci. Curabitur in turpis eleifend, consectetur quam in, convallis urna. Suspendisse euismod lectus vel commodo feugiat.</p>
  <svg class="arrow-btn" style="left:228px" viewBox="0 0 38 38"><circle cx="19" cy="19" r="17" fill="#fff" stroke="var(--orange)" stroke-width="2"/><path d="M22 12l-7 7 7 7M15 19h11" fill="none" stroke="var(--orange)" stroke-width="2"/></svg>
  <div class="showcase hex">
    <div class="img showcase__inner hex">
      <div class="img sofa" role="img" aria-label="Product photograph of a navy velvet sectional sofa with cushions"></div>
    </div>
  </div>
  <svg class="arrow-btn" style="left:932px" viewBox="0 0 38 38"><circle cx="19" cy="19" r="17" fill="#fff" stroke="var(--blue)" stroke-width="2"/><path d="M16 12l7 7-7 7M23 19H12" fill="none" stroke="var(--blue)" stroke-width="2"/></svg>
</section>

<!-- PRODUCT GRID -->
<section>
  <div class="tile tile--light" style="left:0;top:1887px;width:665px;height:293px">
    <div style="position:absolute;left:33px;top:76px;width:230px">
      <h3 class="tile__title">Lorem Ipsum<br>Adipiscing</h3>
      <p class="tile__text">Lorem ipsum dolor sit amet, consectetur adipiscing elit. Vestibulum vestibulum risus in enim accumsan porttitor sed eu orci.</p>
      <span class="tile__more">More <svg width="10" height="8" viewBox="0 0 10 8"><path d="M0 4h8M5 1l3 3-3 3" fill="none" stroke="currentColor" stroke-width="1.4"/></svg></span>
    </div>
    <div class="img" style="left:284px;top:60px;width:360px;height:170px;background:linear-gradient(180deg,#bdbdbd,#8e8e8e 70%,#3a2a22);border-radius:4px" role="img" aria-label="Product photograph of a grey tufted sofa with dark side table"></div>
  </div>

  <div class="tile tile--slate" style="left:665px;top:1887px;width:268px;height:293px">
    <svg class="img" style="left:0;top:0" width="268" height="293" viewBox="0 0 268 293"><path d="M120 293L268 120V293Z" fill="var(--slate-light)"/></svg>
    <div style="position:absolute;left:0;top:22px;width:268px;text-align:center">
      <h3 class="tile__title">Lorem Ipsum<br>Adipiscing</h3>
      <p class="tile__text" style="margin:6px 30px 0">Lorem ipsum dolor sit amet, consectetur adipiscing elit. Vestibulum</p>
    </div>
    <div class="img" style="left:45px;top:125px;width:170px;height:154px;background:linear-gradient(135deg,#d6c48a,#8a7a4a 50%,#2a2a2a)" role="img" aria-label="Product photograph of brass nesting tables"></div>
  </div>

  <div class="tile tile--blue" style="left:933px;top:1887px;width:267px;height:589px">
    <svg class="img" style="left:0;top:0" width="267" height="589" viewBox="0 0 267 589"><path d="M0 330L267 200V589H0Z" fill="var(--blue-deep)"/></svg>
    <div class="img" style="left:37px;top:8px;width:190px;height:342px;background:linear-gradient(180deg,#b89a5a,#7a6236 60%,#2a2018)" role="img" aria-label="Product photograph of a gold woven dining chair"></div>
    <div style="position:absolute;left:0;top:425px;width:267px;text-align:center">
      <h3 class="tile__title">Lorem Ipsum<br>Adipiscing</h3>
      <p class="tile__text" style="margin:6px 24px 0">Lorem ipsum dolor sit amet, consectetur adipiscing elit. Vestibulum vestibulum risus in enim accumsan porttitor.</p>
      <span class="tile__more">More <svg width="10" height="8" viewBox="0 0 10 8"><path d="M0 4h8M5 1l3 3-3 3" fill="none" stroke="currentColor" stroke-width="1.4"/></svg></span>
    </div>
  </div>

  <div class="tile tile--orange" style="left:0;top:2180px;width:331px;height:296px">
    <svg class="img" style="left:0;top:0" width="331" height="296" viewBox="0 0 331 296"><path d="M0 0H331L0 180Z" fill="#f58a45"/></svg>
    <div class="img" style="left:0;top:17px;width:237px;height:170px;background:linear-gradient(135deg,#c9c2b6,#8d8478 60%,#5a4a3c);border-radius:0 60px 20px 0" role="img" aria-label="Product photograph of a taupe upholstered lounge chair"></div>
    <div style="position:absolute;right:24px;top:194px;width:260px;text-align:right">
      <h3 class="tile__title">Lorem Ipsum<br>Adipiscing</h3>
      <p class="tile__text" style="margin-top:4px">Lorem ipsum dolor sit amet, consectetur adipiscing elit. Vestibulum vestibulum</p>
    </div>
  </div>

  <div class="tile tile--white" style="left:331px;top:2180px;width:602px;height:296px">
    <div style="position:absolute;left:24px;top:28px;width:200px">
      <h3 class="tile__title">Lorem Ipsum<br>Adipiscing</h3>
      <p class="tile__text">Lorem ipsum dolor sit amet, consectetur adipiscing elit. Vestibulum vestibulum risus in enim accumsan porttitor sed eu orci.</p>
      <span class="tile__more">More <svg width="10" height="8" viewBox="0 0 10 8"><path d="M0 4h8M5 1l3 3-3 3" fill="none" stroke="currentColor" stroke-width="1.4"/></svg></span>
    </div>
    <div class="img" style="left:190px;top:30px;width:400px;height:230px;background:linear-gradient(160deg,#4a7ad6,#2a58b8 55%,#3a2a22);border-radius:90px 20px 20px 40px" role="img" aria-label="Product photograph of a blue velvet chaise longue with wooden legs"></div>
  </div>
</section>

<!-- NEWS -->
<section>
  <h2 class="sec-title" style="top:2530px">Letest News</h2>
  <p class="sec-lede" style="top:2572px">Lorem ipsum dolor sit amet, consectetur adipiscing elit. Vestibulum vestibulum risus in enim accumsan porttitor sed eu orci. Curabitur in turpis eleifend, consectetur quam in, convallis urna.</p>

  <article class="news-card" style="left:230px">
    <div class="news-card__photo" style="background:linear-gradient(180deg,#c2b2a0,#8aa8c0 45%,#7a5a40)" role="img" aria-label="Photograph of a terrace lounge overlooking a pool">
      <div class="news-card__meta"><span>By: Lorem Ipsum</span><span>25 Oct 2017</span></div>
      <div class="news-card__avatar" role="img" aria-label="Author portrait"></div>
    </div>
    <h3 class="news-card__title">Lorem Ipsum Dolor<br>Consectetur</h3>
  </article>

  <article class="news-card" style="left:483px">
    <div class="news-card__photo" style="background:linear-gradient(180deg,#d8d2c8,#b85a3a 50%,#6a4a3a)" role="img" aria-label="Photograph of an office interior with orange workstations">
      <div class="news-card__meta"><span>By: Lorem Ipsum</span><span>25 Oct 2017</span></div>
      <div class="news-card__avatar" role="img" aria-label="Author portrait"></div>
    </div>
    <h3 class="news-card__title">Lorem Ipsum Dolor<br>Consectetur</h3>
  </article>

  <article class="news-card" style="left:736px">
    <div class="news-card__photo" style="background:linear-gradient(180deg,#d0d0d0,#8a8a8a 55%,#3a3a3a)" role="img" aria-label="Black and white photograph from a charity fashion event">
      <div class="news-card__meta"><span>By: Lorem Ipsum</span><span>25 Oct 2017</span></div>
      <div class="news-card__avatar" role="img" aria-label="Author portrait"></div>
    </div>
    <h3 class="news-card__title">Lorem Ipsum Dolor<br>Consectetur</h3>
  </article>
</section>

<!-- CONTACT -->
<section class="contact">
  <div class="img contact__shade" role="img" aria-label="Darkened photograph of a furnished patio lounge"></div>
  <h2 class="sec-title" style="top:58px">Quick Contact Us</h2>
  <p class="sec-lede" style="top:96px">Lorem ipsum dolor sit amet, consectetur adipiscing elit. Vestibulum vestibulum risus in enim accumsan porttitor sed eu orci. Curabitur in turpis eleifend, consectetur quam in, convallis urna. Suspendisse euismod lectus vel commodo feugiat.</p>
  <div class="field" style="left:230px;top:151px">Your Name*</div>
  <div class="field" style="left:230px;top:193px">Your Email*</div>
  <div class="field" style="left:230px;top:236px">Your Phone*</div>
  <div class="field field--message">Message*</div>
  <a class="btn btn--orange btn--pill" style="left:521px;top:293px;width:160px;height:42px">Send</a>
</section>

<!-- FOOTER -->
<footer class="footer">
  <div class="footer__links">
    <span>Home</span><span class="sep">|</span><span>About Us</span><span class="sep">|</span><span>Our Services</span><span class="sep">|</span><span>Shop</span><span class="sep">|</span><span>Blog</span><span class="sep">|</span><span>Contact Us</span>
  </div>
  <p class="footer__copy">© Copyright 2018 Lorivel Home Studio. All rights reserved.</p>
  <div class="footer__social"><span></span><span></span><span></span><span></span><span></span></div>
</footer>

</body>
</html>
```